Defense contractor needs a flyer for an exhibition

We need a flyer that we can hand out on an exhibition.
For information about our company and product visit:
https://www.brightquillmetrics.com/
I have supplied my business card that you can copy the logo and the contact information. the contact information should be on the last page. It would be nice if you would orient on existing publications of my company.

Important:
For designing you must use Adobe Illustrator/Photoshop and the templates provided in the zip file, to guarantee a perfect print. That means also that you have to use CMYK colors.
The flyer has altogether 6 pages by folding. Every side of the 105mm x 210mm paper contains 3 pages. The folding procedure is called "letterfold".

I think CartPlan2 and HallwayPlan are the best schematics. They should be somehow included in the flyer.

Target Market(s)

Defense

Industry/Entity Type

Defense

Font styles to use
Serif

Colors
0054AA
0677BA
7BADD7
CADEEF
E8F1F8

Requirements
Must have
• black and blue colors should dominate, the template in the zip files must be used
Nice to have
• I would suggest, that you reuse the picture of the tank in front of the sunset.

```html
<!DOCTYPE html>
<html lang="en">
<head>
<meta charset="utf-8">
<title>Advanced Combat Training Systems – Letterfold Flyer</title>
<link href="https://fonts.googleapis.com/css2?family=Bebas+Neue&family=Oswald:wght@300;400&family=Montserrat:wght@400;600;700&display=swap" rel="stylesheet">
<style>
  :root{
    --navy:#211e5e;
    --navy-deep:#14123f;
    --ink:#1b1a4f;
    --sky:#1e9fe3;
    --sky-dark:#0677ba;
    --pale:#e6e8f5;
    --paper:#ffffff;
    --stage:#f4f4f2;
    --white:#ffffff;
    --grey-url:#8d8fa6;
  }
  *{margin:0;padding:0;box-sizing:border-box}
  html,body{width:1119px;height:1200px;overflow:hidden;background:var(--stage)}
  body{position:relative;font-family:'Montserrat',sans-serif;color:var(--ink)}
  .spread{position:absolute;left:166px;width:786px;height:571px;display:grid;grid-template-columns:262px 262px 262px;overflow:hidden}
  .spread--outside{top:22px}
  .spread--inside{top:606px}
  .panel{position:relative;height:571px;overflow:hidden}
  .display{font-family:'Bebas Neue',sans-serif;font-weight:400;line-height:.9}
  .thin{font-family:'Oswald',sans-serif;font-weight:300}
  .brand{font-family:'Montserrat',sans-serif;font-weight:700;color:var(--white);letter-spacing:.02em;text-transform:uppercase}

  /* outside – left panel */
  .panel--intro{background:var(--navy);color:var(--white)}
  .intro-text{position:absolute;left:30px;right:28px;top:22px}
  .intro-text h3{font-size:11px;font-weight:600;margin:0 0 8px}
  .intro-text p{font-size:7.6px;line-height:1.38;margin-bottom:15px}
  .schematic{position:absolute;left:0;right:0;bottom:0;height:186px;background:linear-gradient(160deg,#f4f5fb,#d9dcef)}
  .accent{position:absolute;top:0;right:0;width:40px;height:42px}

  /* outside – photo background */
  .sunset{position:absolute;left:262px;top:0;width:524px;height:571px;
    background:linear-gradient(180deg,var(--navy) 0%,#2c2a6a 24%,#6b4f80 40%,#d47a62 52%,#e8926a 58%,#4a2c3a 66%,#0d0c1c 72%,#0b0b14 100%)}
  .panel--contact,.panel--cover{background:transparent;color:var(--white);text-align:center}
  .panel--contact .brand{position:absolute;left:0;right:0;top:164px;font-size:15px}
  .company{position:absolute;left:0;right:0;top:234px;font-size:15px;color:var(--sky)}
  .address{position:absolute;left:0;right:0;top:266px;font-size:10px;font-weight:600;line-height:1.35}
  .phone{position:absolute;left:0;right:0;top:313px;font-size:10px;font-weight:600}
  .phone b{font-family:'Oswald',sans-serif;font-weight:400;font-size:18px}
  .email{position:absolute;left:0;right:0;top:348px;font-size:9.5px;font-weight:600}
  .url{font-family:'Oswald',sans-serif;font-weight:300;letter-spacing:.12em;color:var(--grey-url);font-size:12px}
  .panel--contact .url{position:absolute;left:0;right:0;top:374px;color:#b4a6b6}
  .panel--cover .brand{position:absolute;right:26px;top:30px;font-size:15px}
  .cover-title{position:absolute;right:40px;top:104px;text-align:right}
  .cover-title .advanced{font-size:63px;color:var(--sky)}
  .cover-title .combat{font-size:80px;color:var(--white)}
  .cover-title .sub{font-size:19px;letter-spacing:.24em;margin-top:8px;color:var(--white)}
  .panel--cover .url{position:absolute;left:0;right:0;top:494px}

  /* inside */
  .panel--light{background:linear-gradient(180deg,#dfe2f2,#f8f8fc 60%,#ffffff)}
  .panel--features{background:linear-gradient(180deg,var(--navy-deep),var(--navy) 60%,#2a2775);color:var(--white)}
  .kicker{position:absolute;left:0;right:0;top:17px;font-size:15.5px;line-height:1.1;color:var(--sky);text-align:center;white-space:nowrap}
  .headline{position:absolute;left:0;right:0;top:44px;font-size:32px;line-height:1.12;color:var(--ink);text-align:center;white-space:nowrap}
  .illustration{position:absolute;left:12px;right:12px;background:linear-gradient(150deg,#eef0f8,#c9cde6)}
  .accent-rule{position:absolute;left:0;right:0;height:40px}
  .body-copy{position:absolute;left:16px;right:16px;font-size:8.6px;line-height:1.42}
  .body-copy strong{font-size:11px;font-weight:600;color:#2a2680;line-height:1.3}
  .body-copy h4{font-size:12px;font-weight:600;color:#2a2680}
  .tagline{position:absolute;left:14px;right:10px;top:420px;white-space:nowrap}
  .tagline .line1{font-size:20px;color:var(--sky)}
  .tagline .line1 span{color:var(--ink)}
  .tagline .line2{font-size:34px;color:var(--ink);margin-top:2px}
  .silhouettes{position:absolute;left:0;right:0;bottom:0;height:58px;background:linear-gradient(180deg,rgba(20,18,63,0) 0%,rgba(20,18,63,.55) 50%,var(--navy-deep) 100%)}

  .features{position:absolute;left:14px;right:18px;top:14px}
  .features h2{font-size:23px;color:var(--sky);margin-bottom:10px}
  .features p{font-size:7.5px;line-height:1.32;text-align:justify}
  .features h5{font-size:8.3px;font-weight:600;margin:9px 0 6px}
</style>
</head>
<body>

<section class="spread spread--outside">
  <div class="sunset" role="img" aria-label="Photo: silhouette of a main battle tank in grass against a dramatic orange sunset sky"></div>

  <article class="panel panel--intro">
    <div class="intro-text">
      <h3>Duel Simulation with TRAXIS</h3>
      <p>TRAXIS is designed to surpass laser engagement system capabilities by achieving realistic training environments, hit detection, and soldier assessment and reaction to battle grounds and conditions. Instructors equipped with TRAXIS have the advantage of full overview, remote weapons blocking and camera control, and mediation among vehicle teams and units with real-time data delivered across multiple instructor workstations simultaneously for safe real-world training environments and results.</p>
      <h3>Firing Range Training with TRAXIS</h3>
      <p>TRAXIS gives instructors complete visual, audio, and data oversight of firing range performance along with camera and weapons blocking control for optimal safety, ammunitions selection and conservation, target precision, and crew instruction.</p>
      <h3>Driving Training with TRAXIS</h3>
      <p>Vehicle teams with TRAXIS have increased vision, awareness, response times, and instructor assistance with control functions during driving training. TRAXIS offers cost-effective safety and driving training solutions in both combat and non-combat modes.</p>
    </div>
    <div class="schematic" role="img" aria-label="Schematic: instructor classroom with wall screens and workstation desks">
      <svg class="accent" viewBox="0 0 40 42" aria-hidden="true"><polygon points="40,0 40,4 4,42 0,42 34,0" fill="var(--sky)"/></svg>
    </div>
  </article>

  <article class="panel panel--contact">
    <div class="brand">Brightquill Metrics</div>
    <div class="company display">Norvale Leitsysteme Jonas Brecht</div>
    <div class="address">Lindenweg 14<br>80331 Musterstadt, Germany</div>
    <div class="phone">Telephone: <b>+49 170 555 0192</b></div>
    <div class="email">Jonas.Brecht@BrightquillMetrics.co</div>
    <div class="url">WWW.BRIGHTQUILLMETRICS.COM</div>
  </article>

  <article class="panel panel--cover">
    <div class="brand">Brightquill Metrics</div>
    <div class="cover-title">
      <div class="display advanced">ADVANCED</div>
      <div class="display combat">COMBAT</div>
      <div class="thin sub">TRAINING SYSTEMS</div>
    </div>
    <div class="url">WWW.BRIGHTQUILLMETRICS.COM</div>
  </article>
</section>

<section class="spread spread--inside">
  <article class="panel panel--light">
    <div class="kicker thin">ADVANCED COMBAT TRAINING SYSTEMS</div>
    <div class="headline display">FOR REALISTIC<br>COMBAT SIMULATION</div>
    <div class="illustration" style="top:122px;height:166px" role="img" aria-label="Schematic CartPlan2: armoured vehicles linked to an instructor command truck with screens"></div>
    <svg class="accent-rule" style="top:288px" viewBox="0 0 262 40" preserveAspectRatio="none" aria-hidden="true"><polygon points="0,8 262,2 236,34 230,34 250,7 0,10" fill="var(--sky)"/></svg>
    <div class="body-copy" style="top:304px">
      <strong>TRAXIS (Tactical Range And eXercise Instrumentation System)</strong> allows for a modern approach to duel simulation, firing range training, armored vehicle driving training, and simulation debriefing through an integrated system of sensors, optics, and controls that give soldiers and instructors real-time, real-world vision and data.
    </div>
    <div class="tagline">
      <div class="display line1">EQUIP YOUR <span>FIGHTING FORCE</span> WITH</div>
      <div class="display line2">PRECISION TRAINING</div>
    </div>
    <div class="silhouettes" role="img" aria-label="Illustration: silhouettes of tanks and soldiers on a grass horizon"></div>
  </article>

  <article class="panel panel--features">
    <div class="features">
      <h2 class="display">FEATURES OF TRAXIS</h2>
      <p>Fully deployed in 20 minutes or less, TRAXIS is uniquely designed to outfit armored vehicles and weapons systems including MBTs, armored IFVs and more regardless of manufacturer type with an array of advanced sensors and instrumentation for the most realistic and productive combat simulation achievable.</p>
      <h5>• Remote-Control Functions</h5>
      <p>Remote weapons blocking and camera control for integrated instruction management and safety</p>
      <h5>• 16 Camera Systems per vehicle</h5>
      <p>Supports up to 16 remote-controlled cameras with pan, tilt, zoom, and thermal / night vision compatibility</p>
      <h5>• Optics Camera</h5>
      <p>Periscope optics camera placement allows for real-time instructor visibility of training grounds, targets, and crew performance</p>
      <h5>• Vehicle Data</h5>
      <p>Lead angles, ammunition types, speed, acceleration, turn indicators, temperature, and positions are shown on an interactive map</p>
      <h5>• Full Instructor Overview with Audio, Visuals, Vehicle Data, and Camera Control</h5>
      <p>Live-stream radio, audio, visual, and sensor data overview with camera controls integrated with instructor command vehicle</p>
      <h5>• Air-Conditioned Instructor Command Workstation</h5>
      <p>Instructor workstation comfort control for optimal focus, precision, and command</p>
      <h5>• Full Data Recording</h5>
      <p>Audio, visual, and sensor data for debriefing, archiving, and performance metrics</p>
      <h5>• All-Weather and All-Terrain</h5>
      <p>Designed for durability and compatibility in any type of weather or terrain scenario</p>
    </div>
  </article>

  <article class="panel panel--light">
    <div class="kicker thin">ADVANCED COMBAT TRAINING SYSTEMS</div>
    <div class="headline display" style="top:46px">HALLWAYPLAN</div>
    <div class="illustration" style="top:96px;height:148px" role="img" aria-label="Schematic HallwayPlan: training room with wall screens and rows of instructor desks"></div>
    <svg class="accent-rule" style="top:248px" viewBox="0 0 262 40" preserveAspectRatio="none" aria-hidden="true"><polygon points="0,10 262,2 236,36 230,36 250,8 0,12" fill="var(--sky)"/></svg>
    <div class="body-copy" style="top:276px">
      <h4>Debriefing with TRAXIS</h4>
      TRAXIS equips instructors with comprehensive data collection of training elements allowing for an immersive, insightful, and detailed debriefing process. All data contents can be easily recorded, edited, and archived for reference. TRAXIS features mobile container functionality for rapid deployment or a compact stationary workplace.
      <h4 style="margin-top:18px">TRAXIS CUSTOMIZATION</h4>
      Get in touch with our development team to plan, design, and implement a TRAXIS system within custom vehicle and infrastructure parameters to achieve unique cost and training utilization goals.
    </div>
    <div class="silhouettes" role="img" aria-label="Illustration: silhouettes of a tank, soldiers and a mortar crew on a grass horizon"></div>
  </article>
</section>

</body>
</html>
```